TR & Groundworks
Landscaping
TR & Groundworks - Utilities
Creative Brief
Professional
Dennis Holloway
Brisk Meadow Cooling and Yardcraft LLP
P.O. Box 618207 Christiansted, St. Croix 00822
Briskmeadowcoolingandyardcraft@mailvessel.com
Mona Fairweather is the Co-Owner name needs to be on card also

```html
<!DOCTYPE html>
<html lang="en">
<head>
<meta charset="utf-8">
<title>Brisk Meadow Cooling and Yardcraft LLP – Business Card</title>
<link rel="stylesheet" href="https://fonts.googleapis.com/css2?family=Arimo:wght@400;700&family=Tinos:wght@700&display=swap">
<style>
  :root {
    --canvas: #ffffff;
    --card-border: #c9c9c9;
    --navy: #1d2a6e;
    --green: #2f8a2a;
    --name-blue: #1b7ec4;
    --ink: #3a3a3a;
    --muted: #6d6d6d;
    --rule: #d6d6d6;
    --blue-light: #6cc4f5;
    --blue-mid: #2f9be2;
    --blue-deep: #147bc6;
    --white: #ffffff;
  }
  * { margin: 0; padding: 0; box-sizing: border-box; }
  html, body {
    width: 1200px; height: 334px; overflow: hidden;
    background: var(--canvas);
  }
  .sheet { position: relative; width: 1200px; height: 334px; }

  .card {
    position: absolute; top: 12px; width: 576px; height: 310px;
  }
  .card--front {
    left: 12px; background: var(--white);
    border: 1px solid var(--card-border);
  }
  .card--back {
    left: 612px;
    background: radial-gradient(ellipse 70% 85% at 58% 50%, var(--blue-light) 0%, var(--blue-mid) 55%, var(--blue-deep) 100%);
  }

  .sans { font-family: "Arimo", Arial, sans-serif; }
  .serif { font-family: "Tinos", "Times New Roman", serif; font-weight: 700; }

  .holder {
    position: absolute; left: 12px; top: 26px;
    font-size: 19px; color: var(--name-blue);
  }
  .co-owner {
    position: absolute; left: 12px; top: 52px;
    font-size: 14px; color: var(--name-blue);
  }
  .license {
    position: absolute; font-size: 12px; color: var(--navy); white-space: nowrap;
  }
  .card--front .license { left: 44px; top: 126px; }
  .wordmark {
    position: absolute; left: 42px; top: 142px;
    font-size: 39px; line-height: 1; color: var(--navy); white-space: nowrap;
  }
  .tagline {
    position: absolute; left: 44px; top: 196px;
    font-size: 15px; color: var(--green); white-space: nowrap;
  }
  .divider {
    position: absolute; left: 312px; top: 122px;
    width: 2px; height: 112px;
    background: linear-gradient(to bottom, rgba(150,150,150,0), #8c8c8c 50%, rgba(150,150,150,0));
  }
  .contact {
    position: absolute; left: 346px; top: 136px;
    font-size: 13px; line-height: 19px; color: var(--ink); font-style: normal;
  }
  .contact .gap { height: 24px; }
  .email-rule {
    position: absolute; left: 12px; right: 12px; top: 274px;
    height: 1px; background: var(--rule);
  }
  .email {
    position: absolute; left: 0; right: 0; top: 284px;
    text-align: center; font-size: 12px; color: var(--muted);
  }

  .card--back .license { left: 236px; top: 104px; color: var(--white); }
  .card--back .wordmark { left: 140px; top: 120px; font-size: 52px; color: var(--white); }
  .card--back .tagline { left: 142px; top: 186px; font-size: 16px; color: var(--white); }
</style>
</head>
<body>
<div class="sheet">
  <section class="card card--front">
    <p class="holder sans">Dennis Holloway</p>
    <p class="co-owner sans">Mona Fairweather, Co-Owner</p>
    <p class="license sans">License No. 472916</p>
    <h1 class="wordmark serif">Brisk Meadow</h1>
    <p class="tagline serif">Cooling and Yardcraft LLP</p>
    <div class="divider"></div>
    <address class="contact sans">
      <div>P.O. Box 618207</div>
      <div>Christiansted,</div>
      <div>St. Croix 00822</div>
      <div class="gap"></div>
      <div>Phone : 340-555-0142</div>
      <div>Cell : 340-555-0187</div>
    </address>
    <div class="email-rule"></div>
    <p class="email sans">Briskmeadowcoolingandyardcraft@mailvessel.com</p>
  </section>

  <section class="card card--back">
    <p class="license sans">License No. 472916</p>
    <h2 class="wordmark serif">Brisk Meadow</h2>
    <p class="tagline serif">Cooling and Yardcraft LLP</p>
  </section>
</div>
</body>
</html>
```